VLM8 Print + Graphic Design

We have already used draft hive for our logo design, which has come out really well. Right now we also running a design contest for our business card, please feel free to participate (contest name: VLM8 Business Card Design Project).
We have our logo design completed and we want the creative designers to now come out with all the other designs for VLM8 needs,
1. Brochure design based on the logo colours (4-8 pages)
2. Tri fold flyer designs based on the logo colours
3. Powerpoint templates for our presentations
4. Letter head designs (A4 & A3)
5. Tech Cases (http://www.brantholm.com.au/webapp/wcs/stores/servlet/ProductDisplay?storeId=47819&langId=10&catalogId=31870&categoryId=512947&productId=48203916&imagePath=QTB0042907)
There should be synergy and continuance across all designs, we use a lot of power-point presentations and continued changes to brochures, so we need these to stand out in graphic design with elegance and class.
Powerpoint / Brochure / Flyer should have the following,
1. Place for photos, charts, texts and sections.
2. Final page to contain our contact details (social + mobile + address)
3. Templates editable by word or powerpoint or illustrator
Thank you and all the best.
For details about the company please visit, www.vlm8.com.
visit www.vlm8.com
Graphic Design

```html
<!DOCTYPE html>
<html lang="en">
<head>
<meta charset="utf-8">
<title>VLM8 Powerpoint Presentation (set 02)</title>
<link rel="stylesheet" href="https://fonts.googleapis.com/css2?family=Crimson+Pro:ital,wght@0,400;1,400&family=PT+Sans+Narrow&family=PT+Sans&display=swap">
<style>
  :root {
    --backdrop: #2b2e2e;
    --heading-green: #a9c94a;
    --lime: #b3d33f;
    --lime-tab: #b5d334;
    --teal: #5bbf8f;
    --teal-dark: #49ae7d;
    --logo-teal: #3fae8c;
    --paper: #ffffff;
    --body-grey: #7b7b7b;
    --ink: #1d1d1d;
  }
  * { box-sizing: border-box; margin: 0; padding: 0; }
  html, body { width: 1200px; height: 748px; overflow: hidden; }
  body {
    background: var(--backdrop);
    font-family: "PT Sans", sans-serif;
    position: relative;
  }
  .sheet-title {
    position: absolute; top: 28px; left: 0; width: 1200px;
    text-align: center;
    font-family: "Crimson Pro", serif;
    font-size: 27px; color: var(--heading-green); font-weight: 400;
  }
  .slide-card { position: absolute; width: 488px; }
  .slide-card.p5 { left: 79px; top: 92px; }
  .slide-card.p6 { left: 647px; top: 92px; }
  .slide-card.p7 { left: 79px; top: 417px; }
  .slide-card.p8 { left: 647px; top: 417px; }

  .slide { position: relative; width: 488px; height: 274px; background: var(--paper); overflow: hidden; }
  .slide .top-tab { position: absolute; left: 0; top: 0; width: 112px; height: 11px; background: var(--lime-tab); }
  .brand { position: absolute; left: 8px; top: 24px; display: flex; align-items: center; gap: 5px; }
  .brand .brand-dot { width: 14px; height: 14px; border-radius: 50%; background: var(--lime); }
  .brand .brand-name {
    font-family: "PT Sans", sans-serif; font-size: 22px; color: var(--logo-teal); letter-spacing: 0.5px; line-height: 1;
  }
  .side-panel { position: absolute; left: 0; top: 61px; width: 107px; height: 178px; background: var(--lime); }
  .side-panel .section-name {
    position: absolute; left: 20px; top: 6px;
    font-family: "PT Sans Narrow", sans-serif; font-size: 21px; color: var(--paper); letter-spacing: 0.3px;
  }
  .side-panel .topic-icon { position: absolute; right: 10px; top: 98px; }
  .photo { position: absolute; left: 109px; top: 61px; width: 134px; height: 81px; }
  .photo.food { background: linear-gradient(135deg, #6b4a33 0%, #b8452c 45%, #d9a36a 75%, #7d8a3c 100%); }
  .photo.childcare { background: linear-gradient(135deg, #e8d6b0 0%, #d6453a 40%, #f0c9a8 70%, #c9b88a 100%); }
  .photo.lighting { background: radial-gradient(circle at 45% 55%, #d9f29a 0%, #5bb23a 35%, #1f5a1e 75%, #0f2e10 100%); }
  .photo.sports { background: linear-gradient(110deg, #6a4d3a 0%, #a8825e 35%, #e4d9c8 60%, #c9c2b8 100%); }
  .topic-box { position: absolute; left: 109px; top: 142px; width: 134px; height: 97px; background: var(--teal); }
  .topic-label {
    position: absolute; left: 6px; top: 12px; width: 124px;
    font-family: "PT Sans Narrow", sans-serif; font-size: 14px; color: var(--paper); line-height: 15px;
    display: flex; gap: 4px;
  }
  .topic-label .chev { font-size: 13px; }
  .topic-label .num { color: var(--ink); }
  .topic-copy {
    position: absolute; left: 252px; top: 57px; width: 216px;
    font-size: 7.3px; line-height: 11.1px; color: var(--body-grey);
  }
  .topic-copy p + p { margin-top: 11px; }
  .slide-footer {
    position: absolute; left: 0; top: 252px; width: 488px; height: 22px;
    background: linear-gradient(90deg, var(--teal-dark), var(--teal));
    color: var(--paper); font-size: 6.6px;
  }
  .slide-footer .address { position: absolute; left: 9px; top: 7px; }
  .slide-footer .footer-dot { position: absolute; left: 249px; top: 6px; width: 10px; height: 10px; border-radius: 50%; background: var(--paper); }
  .slide-footer .company { position: absolute; left: 275px; top: 7px; }
  .slide-footer .pager { position: absolute; right: 7px; top: 5px; display: flex; align-items: center; gap: 4px; font-size: 7px; }
  .page-caption {
    margin-top: 7px; text-align: right;
    font-family: "Crimson Pro", serif; font-style: italic; font-size: 17px; color: var(--heading-green);
  }
</style>
</head>
<body>
  <h1 class="sheet-title">Powerpoint Presentation (set 02)</h1>

  <!-- Page 5 -->
  <section class="slide-card p5">
    <div class="slide">
      <div class="top-tab"></div>
      <div class="brand"><span class="brand-dot"></span><span class="brand-name">VLM8</span></div>
      <div class="side-panel"><span class="section-name">SERVICES</span></div>
      <div class="photo food" role="img" aria-label="Photo of a table of assorted dishes, grilled food and red chillies"></div>
      <div class="topic-box">
        <div class="topic-label"><span class="chev">&gt;</span><span><span class="num">02</span> FOOD SERVICES</span></div>
      </div>
      <div class="topic-copy">
        <p>“One cannot think well, love well, sleep well, if one has not dined well.” — Mara Ellison, A Table of One's Own VLM8 envisions its foray into the food industry bringing diversified cultures and cuisines into one channel. Our biggest aim is to establish this channel of opportunities between countries who have rich worldly cuisines from dine-in restaurants to Chocolatiers.</p>
      </div>
      <div class="slide-footer">
        <span class="address">118 Harbor Row 03, 6th Lane Westmoor, Kelvale, Dunmore, 738410</span>
        <span class="footer-dot"></span>
        <span class="company">VLM8 Pty Ltd</span>
        <span class="pager">
          <svg width="6" height="8" viewBox="0 0 6 8"><path d="M5 1 L2 4 L5 7" stroke="#fff" stroke-width="1.6" fill="none"/></svg>05
          <svg width="6" height="8" viewBox="0 0 6 8"><path d="M1 1 L4 4 L1 7" stroke="#fff" stroke-width="1.6" fill="none"/></svg>
        </span>
      </div>
    </div>
    <p class="page-caption">5th page</p>
  </section>

  <!-- Page 6 -->
  <section class="slide-card p6">
    <div class="slide">
      <div class="top-tab"></div>
      <div class="brand"><span class="brand-dot"></span><span class="brand-name">VLM8</span></div>
      <div class="side-panel">
        <span class="section-name">SERVICES</span>
        <svg class="topic-icon" width="7" height="11" viewBox="0 0 7 11"><circle cx="3.5" cy="2" r="2" fill="#fff"/><rect x="1" y="4.5" width="5" height="6" rx="1.5" fill="#fff"/></svg>
      </div>
      <div class="photo childcare" role="img" aria-label="Photo of a carer and a child playing with building blocks"></div>
      <div class="topic-box">
        <div class="topic-label"><span class="chev">&gt;</span><span><span class="num">03</span> CHILD CARE<br>CENTRES</span></div>
      </div>
      <div class="topic-copy">
        <p>VLM8 is committed to establish early learning centres across developing countries. In the current market, there are many busy professionals with families. Every working parent requires a peace of mind that their child has been well looked after at the day care centres.</p>
        <p>Our vision is to provide quality and nurturing day care environment. We promise to open strictly follow Child care rules and legislations of the country and in parallel to catering for every child's requirements whether its learning or nutrition</p>
      </div>
      <div class="slide-footer">
        <span class="address">118 Harbor Row 03, 6th Lane Westmoor, Kelvale, Dunmore, 738410</span>
        <span class="footer-dot"></span>
        <span class="company">VLM8 Pty Ltd</span>
        <span class="pager">
          <svg width="6" height="8" viewBox="0 0 6 8"><path d="M5 1 L2 4 L5 7" stroke="#fff" stroke-width="1.6" fill="none"/></svg>06
          <svg width="6" height="8" viewBox="0 0 6 8"><path d="M1 1 L4 4 L1 7" stroke="#fff" stroke-width="1.6" fill="none"/></svg>
        </span>
      </div>
    </div>
    <p class="page-caption">6th page</p>
  </section>

  <!-- Page 7 -->
  <section class="slide-card p7">
    <div class="slide">
      <div class="top-tab"></div>
      <div class="brand"><span class="brand-dot"></span><span class="brand-name">VLM8</span></div>
      <div class="side-panel">
        <span class="section-name">SERVICES</span>
        <svg class="topic-icon" width="8" height="11" viewBox="0 0 8 11"><circle cx="4" cy="3.8" r="3.5" fill="#fff"/><rect x="2.4" y="7" width="3.2" height="3.5" fill="#fff"/></svg>
      </div>
      <div class="photo lighting" role="img" aria-label="Photo of a glowing light bulb with green light streaks"></div>
      <div class="topic-box">
        <div class="topic-label"><span class="chev">&gt;</span><span><span class="num">04</span> LIGHTING</span></div>
      </div>
      <div class="topic-copy">
        <p>VLM8 provides in depth knowledge on Lighting technologies varying from Lumora to Brightvale with different product offerings. We partner with organizations with over 15+ years of experience delivering projects of different scale from five star hotels, hospital services, public places, etc.</p>
        <p>We specialize in managing and delivering the project and services end to end - from requirements design, sourcing equipments and implementation.</p>
      </div>
      <div class="slide-footer">
        <span class="address">118 Harbor Row 03, 6th Lane Westmoor, Kelvale, Dunmore, 738410</span>
        <span class="footer-dot"></span>
        <span class="company">VLM8 Pty Ltd</span>
        <span class="pager">
          <svg width="6" height="8" viewBox="0 0 6 8"><path d="M5 1 L2 4 L5 7" stroke="#fff" stroke-width="1.6" fill="none"/></svg>07
          <svg width="6" height="8" viewBox="0 0 6 8"><path d="M1 1 L4 4 L1 7" stroke="#fff" stroke-width="1.6" fill="none"/></svg>
        </span>
      </div>
    </div>
    <p class="page-caption">7th page</p>
  </section>

  <!-- Page 8 -->
  <section class="slide-card p8">
    <div class="slide">
      <div class="top-tab"></div>
      <div class="brand"><span class="brand-dot"></span><span class="brand-name">VLM8</span></div>
      <div class="side-panel">
        <span class="section-name">SERVICES</span>
        <svg class="topic-icon" width="10" height="10" viewBox="0 0 10 10"><circle cx="6" cy="2" r="1.6" fill="#fff"/><path d="M1 5 L5 4 L7 6 L4 9" stroke="#fff" stroke-width="1.4" fill="none"/></svg>
      </div>
      <div class="photo sports" role="img" aria-label="Photo of a climber on a rock face against a hazy sky"></div>
      <div class="topic-box">
        <div class="topic-label"><span class="chev">&gt;</span><span><span class="num">05</span> EXTREME<br>SPORTS</span></div>
      </div>
      <div class="topic-copy">
        <p>We all need gush of adventure from time to time. We do this to push ourselves to feel the adrenalin run through our veins. Whether it's extreme sport or dangerous outdoors which is challenging or trying to push ourselves to the limits to achieve the inner potential, it's all adrenalin that we require.</p>
        <p>VLM8 promises to bring the adventures to you. Plan your next adventure with us.</p>
      </div>
      <div class="slide-footer">
        <span class="address">118 Harbor Row 03, 6th Lane Westmoor, Kelvale, Dunmore, 738410</span>
        <span class="footer-dot"></span>
        <span class="company">VLM8 Pty Ltd</span>
        <span class="pager">
          <svg width="6" height="8" viewBox="0 0 6 8"><path d="M5 1 L2 4 L5 7" stroke="#fff" stroke-width="1.6" fill="none"/></svg>08
          <svg width="6" height="8" viewBox="0 0 6 8"><path d="M1 1 L4 4 L1 7" stroke="#fff" stroke-width="1.6" fill="none"/></svg>
        </span>
      </div>
    </div>
    <p class="page-caption">8th page</p>
  </section>
</body>
</html>
```